Business Cards for Corvantis LLC

We need business cards for a new company called “Corvantis LLC”. This is a technology process improvement company providing a comprehensive assessment of the technology used to run their business. The documentation and review process delivers the visibility and reassurance they need to protect their business and plan for the future. The product is called “Halvorne Ledgerwork”. Our primary target is small-medium size businesses, with the deliverables going to the decision maker. We would like to see the designs use the color blue. Our tag line is SECURE YOUR SYSTEMS · PLAN WITH CLARITY.

Industry/Entity Type

Business

Contact Information for Business Card

Tag line should be on back of card - it does not have to be upper case.

Requirements
Must have
• Please use information when laying out card:
• Name: Darnell Pruitt
• Title: Partner
• Phone Number: (877)555-0143
• Email: dell@corvantisllc.com
• Website: http://corvantisllc.com

```html
<!DOCTYPE html>
<html lang="en">
<head>
<meta charset="UTF-8">
<title>Corvantis LLC – Business Cards</title>
<link href="https://fonts.googleapis.com/css2?family=Open+Sans:wght@400;600;700&display=swap" rel="stylesheet">
<style>
  :root {
    --canvas: #e9ebee;
    --blue-deep: #1a5f9e;
    --blue-mid: #2a78bf;
    --blue-brand: #2f7cc6;
    --blue-text: #3a7fc0;
    --grey-name: #6b6e72;
    --grey-text: #5d6064;
    --white: #ffffff;
    --card-shadow: rgba(20, 30, 45, 0.22);
  }
  * { box-sizing: border-box; margin: 0; padding: 0; }
  html, body {
    width: 1200px; height: 760px; overflow: hidden;
    background: var(--canvas);
    font-family: "Open Sans", Arial, sans-serif;
  }
  .sheet {
    position: relative; width: 1200px; height: 760px;
    display: flex; align-items: center; justify-content: center; gap: 40px;
  }
  .card {
    position: relative; width: 550px; height: 314px;
    border-radius: 28px; overflow: hidden;
    box-shadow: 0 10px 28px var(--card-shadow);
  }

  /* Back of card */
  .card--back {
    background: linear-gradient(160deg, var(--blue-mid) 0%, var(--blue-deep) 100%);
    color: var(--white);
    display: flex; flex-direction: column; align-items: center; justify-content: center;
  }
  .back-mark {
    width: 30px; height: 30px; border-radius: 50%;
    background: var(--white); margin-bottom: 18px;
  }
  .back-name {
    font-weight: 700; font-size: 44px; letter-spacing: 1px; line-height: 1;
    text-transform: uppercase;
  }
  .tagline {
    margin-top: 38px; font-size: 15px; font-weight: 400; letter-spacing: 0.3px;
    text-transform: uppercase;
  }

  /* Front of card */
  .card--front { background: var(--white); }
  .front-backdrop {
    position: absolute; left: 150px; top: 0; width: 190px; height: 314px;
    background: radial-gradient(ellipse at center, rgba(210,215,222,0.28) 0%, rgba(255,255,255,0) 70%);
  }
  .front-ring {
    position: absolute; left: -40px; top: 70px; width: 230px; height: 230px;
    border: 1px solid #eceef0; border-radius: 50%;
  }
  .front-brand {
    position: absolute; left: 40px; top: 108px; width: 280px;
    display: flex; flex-direction: column; align-items: center; gap: 14px;
  }
  .front-mark { width: 34px; height: 34px; background: var(--blue-brand); }
  .front-name {
    font-weight: 700; font-size: 28px; line-height: 1; color: var(--blue-brand);
    text-transform: uppercase; letter-spacing: 0.5px; white-space: nowrap;
  }
  .contact-block { position: absolute; left: 348px; top: 92px; }
  .person-name { font-size: 21px; font-weight: 600; color: var(--grey-name); }
  .person-role { font-size: 14px; font-weight: 600; color: var(--blue-text); margin-top: 2px; }
  .contact-list { list-style: none; margin-top: 24px; }
  .contact-item {
    display: flex; align-items: center; gap: 10px;
    font-size: 14px; color: var(--grey-text); margin-bottom: 11px;
  }
  .contact-icon { width: 16px; height: 16px; flex: none; }
</style>
</head>
<body>
<main class="sheet">
  <section class="card card--back" aria-label="Back of business card">
    <span class="back-mark"></span>
    <div class="back-name">Corvantis LLC</div>
    <p class="tagline">Secure your systems · Plan with clarity</p>
  </section>

  <section class="card card--front" aria-label="Front of business card">
    <div class="front-backdrop" role="img" aria-label="Faint map outline in the background"></div>
    <div class="front-ring"></div>
    <div class="front-brand">
      <span class="front-mark"></span>
      <span class="front-name">Corvantis LLC</span>
    </div>
    <div class="contact-block">
      <h1 class="person-name">Darnell Pruitt</h1>
      <p class="person-role">Partner</p>
      <ul class="contact-list">
        <li class="contact-item">
          <svg class="contact-icon" viewBox="0 0 16 16" aria-hidden="true"><path fill="#3a7fc0" d="M2 6c0-2 2-3 6-3s6 1 6 3v1h-3V5.5H5V7H2zM4 8h8l1.5 5h-11z"/></svg>
          (877)555-0143
        </li>
        <li class="contact-item">
          <svg class="contact-icon" viewBox="0 0 16 16" aria-hidden="true"><rect x="1" y="3.5" width="14" height="9" rx="1" fill="#3a7fc0"/><path d="M1.5 4l6.5 5 6.5-5" fill="none" stroke="#fff" stroke-width="1.2"/></svg>
          dell@corvantisllc.com
        </li>
        <li class="contact-item">
          <svg class="contact-icon" viewBox="0 0 16 16" aria-hidden="true"><circle cx="8" cy="8" r="6.5" fill="none" stroke="#3a7fc0" stroke-width="1.4"/><ellipse cx="8" cy="8" rx="2.8" ry="6.5" fill="none" stroke="#3a7fc0" stroke-width="1.1"/><path d="M1.5 8h13" stroke="#3a7fc0" stroke-width="1.1"/></svg>
          corvantisllc.com
        </li>
      </ul>
    </div>
  </section>
</main>
</body>
</html>
```